Safety training business card design

We need a buisness card design and logo for a small buisness that provides safety training through out the mining and civil construction industries. We provide first aid , confined space working at heights , machinery tickets, chainsaw, four wheel drive and four wheel motorbike training. We would like to use the design colors of navy blue, Fluro or lime green and white .

Industry/Entity Type

Construction

Contact Information for Business Card

Kelbrook Earthmoving & Training , Dennis Holloway, kelbrook.training@mailbox-example.com, ph 0438615044 abn 47 816 305 971

```html
<!DOCTYPE html>
<html lang="en">
<head>
<meta charset="utf-8">
<title>Kelbrook Earthmoving &amp; Training – Business Card</title>
<link href="https://fonts.googleapis.com/css2?family=Montserrat:wght@600;700&family=Didact+Gothic&display=swap" rel="stylesheet">
<style>
  :root {
    --navy: #0b2150;
    --lime: #6cbd2c;
    --white: #ffffff;
    --paper: #f7f8f6;
    --backdrop: #e9e7e2;
    --faint: rgba(108, 189, 44, 0.10);
  }
  * { box-sizing: border-box; margin: 0; padding: 0; }
  html, body {
    width: 1200px; height: 857px; overflow: hidden;
    background: var(--backdrop);
  }
  .stage {
    width: 1200px; height: 857px;
    display: flex; align-items: center; justify-content: center; gap: 50px;
  }
  .card {
    position: relative; width: 540px; height: 309px; overflow: hidden;
    box-shadow: 0 6px 18px rgba(0,0,0,0.18);
  }

  /* Front */
  .card-front { background: var(--paper); }
  .watermark {
    position: absolute; right: 40px; top: 120px;
    width: 230px; height: 230px; border-radius: 50%;
    background: var(--faint);
  }
  .brand {
    position: absolute; left: 26px; top: 22px;
    display: flex; align-items: center; gap: 10px;
  }
  .brand-dot {
    width: 40px; height: 40px; border-radius: 50%; background: var(--navy);
  }
  .brand-name {
    font-family: "Montserrat", sans-serif; font-weight: 700;
    color: var(--lime); line-height: 1;
  }
  .brand-name .main { display: block; font-size: 34px; letter-spacing: 2px; }
  .brand-name .sub { display: block; font-size: 10.5px; letter-spacing: 1.6px; margin-top: 3px; }
  .name-bar {
    position: absolute; left: 0; top: 100px; width: 370px; height: 34px;
    background: var(--lime);
    display: flex; align-items: center; padding-left: 26px;
    font-family: "Didact Gothic", sans-serif; font-size: 19px;
    color: var(--white); letter-spacing: 0.5px;
  }
  .contact {
    position: absolute; left: 26px; top: 148px;
    font-family: "Didact Gothic", sans-serif; font-size: 14px;
    color: var(--navy); line-height: 1.45;
  }
  .contact .label { color: var(--lime); font-weight: bold; margin-right: 6px; }
  .abn-band {
    position: absolute; left: 0; bottom: 0; width: 100%; height: 44px;
    background: var(--lime);
    display: flex; align-items: center; padding-left: 26px;
    font-family: "Didact Gothic", sans-serif; font-size: 17px;
    color: var(--white); letter-spacing: 5px;
  }

  /* Back */
  .card-back { background: var(--navy); }
  .back-mark {
    position: absolute; inset: 0;
    display: flex; align-items: center; justify-content: center; gap: 12px;
    padding-bottom: 30px;
  }
  .back-mark .square { width: 30px; height: 30px; background: var(--white); }
  .back-mark .word {
    font-family: "Montserrat", sans-serif; font-weight: 700;
    font-size: 36px; letter-spacing: 3px; color: var(--white);
  }
  .back-signoff {
    position: absolute; right: 22px; bottom: 18px; text-align: right;
    font-family: "Montserrat", sans-serif; font-weight: 700;
    color: var(--white); line-height: 1;
  }
  .back-signoff .main { display: block; font-size: 18px; letter-spacing: 1.5px; }
  .back-signoff .sub { display: block; font-size: 6.5px; letter-spacing: 1px; margin-top: 3px; }
</style>
</head>
<body>
<main class="stage">
  <section class="card card-front" aria-label="Business card front">
    <div class="watermark" aria-hidden="true"></div>
    <div class="brand">
      <span class="brand-dot" aria-hidden="true"></span>
      <span class="brand-name">
        <span class="main">KELBROOK</span>
        <span class="sub">EARTHMOVING &amp; TRAINING</span>
      </span>
    </div>
    <div class="name-bar">Dennis Holloway</div>
    <div class="contact">
      <p>kelbrook.training@mailbox-example.com</p>
      <p><span class="label">PH</span>0438615044</p>
    </div>
    <div class="abn-band">ABN 47 816 305 971</div>
  </section>

  <section class="card card-back" aria-label="Business card back">
    <div class="back-mark">
      <span class="square" aria-hidden="true"></span>
      <span class="word">KELBROOK</span>
    </div>
    <div class="back-signoff">
      <span class="main">KELBROOK</span>
      <span class="sub">EARTHMOVING &amp; TRAINING</span>
    </div>
  </section>
</main>
</body>
</html>
```